Infusion box "Lantern Row Makers workshop"

We need a cardboard box design that will carry 2 varieties of 50 gr infusions inside. each, with a size of 5.5 cm wide, 3.2 cm deep and 15.5 cm high.
The phrase "Made by people with disabilities", "BrumaLú", KOV Foundation (logo is attached) must be incorporated.
Background tea leaves can also be incorporated into the design.
We are open to receiving different box alternatives, ideally maintaining a sober design that can be easily assembled.

```html
<!DOCTYPE html>
<html lang="es">
<head>
<meta charset="utf-8">
<title>Té Verde Jengibre – dieline</title>
<link rel="stylesheet" href="https://fonts.googleapis.com/css2?family=Bebas+Neue&family=Dancing+Script:wght@500;700&family=Oswald:wght@500&display=swap">
<style>
  :root {
    --wine: #66022e;
    --ink: #120006;
    --leaf-light: #5a0229;
    --leaf-mid: #3a0118;
    --leaf-deep: #220010;
    --label: #ffffff;
    --label-line: #0b0004;
    --brand-red: #e30613;
    --paper: #ffffff;
    --illustration: #8a6a6a;
  }
  html, body {
    margin: 0;
    width: 720px;
    height: 1200px;
    overflow: hidden;
    background: var(--paper);
  }
  .canvas {
    position: relative;
    width: 720px;
    height: 1200px;
  }
  .dieline {
    position: absolute;
    left: 44px;
    top: 200px;
    width: 632px;
    height: 799px;
  }
  .panel-wine { fill: var(--wine); }
  .panel-side { fill: var(--ink); }
  .leaf-front { fill: url(#leafToneFront); }
  .leaf-back { fill: url(#leafToneBack); }
  .label-oval { fill: var(--label); stroke: var(--label-line); stroke-width: 3; }
  .script { font-family: "Dancing Script", cursive; fill: var(--ink); }
  .title { font-family: "Bebas Neue", "Oswald", sans-serif; fill: var(--wine); }
  .weight { font-family: "Dancing Script", cursive; fill: var(--wine); }
  .brand { font-family: "Oswald", sans-serif; font-weight: 500; fill: var(--brand-red); }
  .brand-box { fill: var(--paper); }
  .illustration { fill: var(--illustration); }
</style>
</head>
<body>
<div class="canvas">
  <svg class="dieline" viewBox="0 0 1021 1288" xmlns="http://www.w3.org/2000/svg">
    <defs>
      <radialGradient id="leafToneFront" cx="50%" cy="50%" r="75%">
        <stop offset="0%" stop-color="var(--leaf-mid)"/>
        <stop offset="55%" stop-color="var(--leaf-light)"/>
        <stop offset="100%" stop-color="var(--leaf-deep)"/>
      </radialGradient>
      <linearGradient id="leafToneBack" x1="0" y1="0" x2="1" y2="1">
        <stop offset="0%" stop-color="var(--leaf-light)"/>
        <stop offset="35%" stop-color="var(--leaf-deep)"/>
        <stop offset="65%" stop-color="var(--leaf-light)"/>
        <stop offset="100%" stop-color="var(--leaf-mid)"/>
      </linearGradient>
    </defs>

    <!-- top closing flap -->
    <rect class="panel-wine" x="191" y="0" width="318" height="191"/>
    <g class="flap-brand">
      <rect class="brand-box" x="325" y="63" width="52" height="15"/>
      <text class="brand" x="351" y="74.5" font-size="9" text-anchor="middle">BrumaLú</text>
      <rect class="brand-box" x="302" y="77" width="96" height="35"/>
      <circle cx="312" cy="94.5" r="5" fill="var(--brand-red)"/>
      <text class="brand" x="320" y="99" font-size="11">KOV Foundation</text>
    </g>

    <!-- main body -->
    <rect class="panel-wine" x="0" y="190" width="1021" height="911"/>

    <!-- decorative band -->
    <rect class="panel-side" x="0" y="363" width="191" height="563"/>
    <rect class="leaf-front" x="191" y="363" width="318" height="563" role="img" aria-label="Dark tea leaf and flower pattern on wine, front panel"/>
    <rect class="panel-side" x="509" y="363" width="191" height="563"/>
    <rect class="leaf-back" x="700" y="363" width="321" height="563" role="img" aria-label="Dark tea leaf and flower pattern on wine, back panel"/>

    <!-- front label -->
    <g class="front-label">
      <ellipse class="label-oval" cx="350" cy="645" rx="130" ry="215"/>
      <text class="script" x="350" y="480" font-size="30" font-weight="500" text-anchor="middle">Tea Blend</text>
      <text class="title" x="350" y="546" font-size="60" text-anchor="middle">TÉ VERDE</text>
      <text class="title" x="350" y="587" font-size="46" text-anchor="middle">JENGIBRE</text>
      <text class="script" x="350" y="617" font-size="15" font-weight="700" text-anchor="middle">Sencha japonés con</text>
      <text class="script" x="350" y="631" font-size="15" font-weight="700" text-anchor="middle">cascara de limón y</text>
      <text class="script" x="350" y="645" font-size="15" font-weight="700" text-anchor="middle">trocitos de jengibre</text>
      <text class="weight" x="350" y="667" font-size="16" font-weight="700" text-anchor="middle">50 g</text>
      <circle class="illustration" cx="350" cy="733" r="57" role="img" aria-label="Ornamental medallion framing a cup of tea"/>
      <text class="brand" x="350" y="820" font-size="5" text-anchor="middle">MADE BY</text>
      <text class="brand" x="350" y="826" font-size="5" text-anchor="middle">PEOPLE WITH DISABILITIES</text>
      <circle cx="312" cy="837" r="5" fill="var(--brand-red)"/>
      <text class="brand" x="320" y="841" font-size="11">KOV Foundation</text>
    </g>

    <!-- bottom closing flap -->
    <rect class="panel-wine" x="191" y="1100" width="318" height="188"/>
  </svg>
</div>
</body>
</html>
```